Web Design Project

I want customers to be able to book appointments to get their makeup done and make a deposit and also have a gallery where i put my portfolio images, i want it to be very simple yet elegant.

Target Market(s)

Women ranging from 18-40 that want to get their makeup done

Industry/Entity Type

Makeup

Font styles to use
Sans Serif
Decorative

Requirements
Nice to have
• easy scheduling option and option to pay service in full on website.

```html
<!DOCTYPE html>
<html lang="en">
<head>
<meta charset="utf-8">
<title>Clara Mae Makeup – Book Appointment Online</title>
<link href="https://fonts.googleapis.com/css2?family=Raleway:wght@200;300;400;500;600&family=Arimo:wght@400;700&display=swap" rel="stylesheet">
<style>
  :root {
    --header-bg: #1b1b1b;
    --band-bg: #2a2a2a;
    --footer-bg: #1f1f1f;
    --copyright-bg: #171717;
    --accent: #b3191f;
    --button: #9e1318;
    --text: #333333;
    --muted: #6b6b6b;
    --light-text: #e4e4e4;
    --panel: #f0f0f0;
    --panel-head: #dcdcdc;
    --bar: #c4c4c4;
    --divider: #4a4a4a;
  }
  * { box-sizing: border-box; margin: 0; padding: 0; }
  html, body { width: 1200px; height: 925px; overflow: hidden; background: #fff; }
  body { position: relative; font-family: "Arimo", Arial, sans-serif; color: var(--text); }

  /* Header */
  .site-header { position: absolute; left: 0; top: 0; width: 1200px; height: 113px; background: var(--header-bg); }
  .brand { position: absolute; left: 240px; top: 30px; display: flex; align-items: center; gap: 10px; }
  .brand-name { font-family: "Raleway", sans-serif; font-weight: 200; font-size: 40px; letter-spacing: 3px; color: #f2f2f2; line-height: 1; }
  .main-nav { position: absolute; left: 508px; top: 45px; display: flex; }
  .nav-item { height: 36px; padding: 0 14px; border-left: 1px solid #dcdcdc; font-family: "Raleway", sans-serif; color: #f2f2f2; }
  .nav-item:first-child { border-left: none; }
  .nav-item .nav-title { display: block; font-size: 12px; font-weight: 500; letter-spacing: .3px; text-transform: uppercase; line-height: 18px; }
  .nav-item .nav-sub { display: block; font-family: "Arimo", sans-serif; font-size: 9px; color: #c9c9c9; margin-top: 4px; }
  .nav-item.active .nav-title { color: var(--accent); }
  .nav-item:nth-child(1) { width: 70px; }
  .nav-item:nth-child(2) { width: 94px; }
  .nav-item:nth-child(3) { width: 93px; }
  .nav-item:nth-child(4) { width: 109px; }
  .nav-item:nth-child(5) { padding-left: 16px; }

  /* Portfolio strip */
  .portfolio-strip { position: absolute; left: 0; top: 113px; width: 1200px; height: 159px; display: flex; }
  .portfolio-tile { width: 120px; height: 159px; }
  .tile-1 { background: linear-gradient(160deg, #2b2320, #c9a08a 55%, #3a2b26); }
  .tile-2 { background: linear-gradient(160deg, #e9e6e3, #d3ad95 50%, #2a2422); }
  .tile-3 { background: linear-gradient(160deg, #2f2520, #b98468 50%, #6b4a38); }
  .tile-4 { background: linear-gradient(160deg, #3b3030, #c8a0a4 50%, #2c2226); }
  .tile-5 { background: linear-gradient(160deg, #8a5e44, #d7a98b 50%, #3a2a22); }
  .tile-6 { background: linear-gradient(160deg, #1c1616, #d0a493 50%, #5c1a1e); }
  .tile-7 { background: linear-gradient(160deg, #151515, #cfa899 55%, #2c2626); }
  .tile-8 { background: linear-gradient(160deg, #111, #dcc4bc 55%, #1c1c1c); }
  .tile-9 { background: linear-gradient(160deg, #2a2424, #d4aa96 50%, #6d1a1f); }
  .tile-10 { background: linear-gradient(160deg, #5a4a40, #e0bba6 55%, #2a2220); }
  .strip-base { position: absolute; left: 0; top: 272px; width: 1200px; height: 13px; background: var(--band-bg); }

  /* Booking */
  .page-title { position: absolute; left: 239px; top: 303px; font-family: "Raleway", sans-serif; font-weight: 400; font-size: 15px; letter-spacing: 1px; text-transform: uppercase; color: var(--accent); }
  .booking { position: absolute; left: 239px; top: 334px; width: 497px; }
  .booking-bar { height: 27px; background: var(--bar); font-size: 11px; font-weight: 700; line-height: 27px; padding-left: 6px; color: #222; }
  .search-panel { position: relative; height: 74px; margin-top: 6px; background: var(--panel); font-size: 9px; }
  .field-label { position: absolute; font-weight: 700; font-size: 9px; color: #111; }
  .service-name { position: absolute; left: 1px; top: 23px; font-size: 10px; color: #555; }
  .service-meta { position: absolute; left: 1px; top: 36px; font-size: 10px; color: #999; }
  .modify-link { position: absolute; left: 0; top: 58px; font-size: 9px; color: #444; }
  .select-box { position: absolute; height: 16px; border: 1px solid #aaa; background: #fff; font-size: 9px; line-height: 14px; padding-left: 4px; }
  .select-box::after { content: ""; position: absolute; right: 0; top: 0; width: 13px; height: 14px; border-left: 1px solid #aaa; background: #eee; }
  .date-input { position: absolute; left: 304px; top: 26px; width: 113px; height: 14px; border: 1px solid #aaa; background: #fff; font-size: 9px; line-height: 12px; padding-left: 3px; }

  .day-tabs { position: absolute; left: 248px; top: 471px; display: flex; align-items: center; gap: 5px; }
  .day-tab { width: 59px; height: 28px; border-radius: 6px; background: #d7d7d7; color: #777; font-size: 9px; text-align: center; line-height: 11px; padding-top: 3px; }
  .day-tab.current { background: #555; color: #fff; font-weight: 700; }
  .day-arrow { width: 14px; color: #bbb; font-size: 16px; text-align: center; }

  .results-heading { position: absolute; left: 265px; top: 523px; font-size: 14px; color: #555; }
  .slots { position: absolute; left: 278px; top: 543px; width: 432px; border-collapse: collapse; font-size: 10px; border: 1px solid #e0e0e0; border-top: none; }
  .slots th { height: 19px; background: linear-gradient(#bdbdbd, #9c9c9c); color: #fff; font-weight: 700; text-align: left; padding-left: 5px; font-size: 10px; }
  .slots td { height: 39px; padding-left: 5px; color: #222; }
  .slots tr:nth-child(odd) td { background: #efefef; }
  .slots tr:nth-child(even) td { background: #fff; }
  .select-button { display: inline-block; width: 52px; height: 19px; background: var(--button); color: #fff; font-size: 10px; line-height: 19px; text-align: center; border-radius: 2px; }

  /* Sidebar */
  .sidebar { position: absolute; left: 750px; top: 333px; width: 215px; height: 270px; background: var(--panel); font-size: 9px; color: var(--muted); }
  .sidebar-head { height: 28px; background: var(--panel-head); font-size: 10px; font-weight: 700; color: #222; line-height: 28px; padding-left: 23px; position: relative; }
  .sidebar-head .head-icon { position: absolute; left: 6px; top: 7px; }
  .help-list { list-style: none; padding: 10px 0 6px 4px; }
  .help-list li { height: 23.5px; }
  .help-list li::before { content: "?"; color: #bbb; margin-right: 5px; }
  .sidebar p { padding: 0 4px; line-height: 11px; margin-top: 6px; }
  .sidebar .login { color: #222; }

  /* Footer */
  .site-footer { position: absolute; left: 0; top: 753px; width: 1200px; height: 133px; background: var(--footer-bg); color: var(--light-text); font-size: 10px; }
  .hours { position: absolute; left: 270px; top: 20px; line-height: 16px; }
  .hours span { display: inline-block; width: 34px; }
  .footer-icon { position: absolute; }
  .cards { position: absolute; left: 271px; top: 88px; display: flex; gap: 2px; }
  .card { width: 30px; height: 20px; border-radius: 2px; }
  .address { position: absolute; left: 532px; top: 18px; line-height: 16px; }
  .phone { position: absolute; left: 532px; top: 73px; font-size: 14px; }
  .social { position: absolute; left: 801px; top: 22px; display: flex; gap: 6px; }
  .social-square { width: 22px; height: 22px; background: #fff; }
  .stores { position: absolute; left: 805px; top: 64px; display: flex; gap: 5px; }
  .store-badge { width: 76px; height: 26px; background: #0c0c0c; border: 1px solid #333; border-radius: 3px; }
  .copyright { position: absolute; left: 0; top: 886px; width: 1200px; height: 39px; background: var(--copyright-bg); color: #aaa; font-size: 10px; text-align: center; line-height: 39px; }
</style>
</head>
<body>

<header class="site-header">
  <div class="brand"><span class="brand-name">CLARA MAE</span></div>
  <nav class="main-nav">
    <div class="nav-item"><span class="nav-title">Home</span><span class="nav-sub">home page</span></div>
    <div class="nav-item"><span class="nav-title">About Us</span><span class="nav-sub">Clara Mae</span></div>
    <div class="nav-item"><span class="nav-title">Portfolio</span><span class="nav-sub">my work</span></div>
    <div class="nav-item"><span class="nav-title">Testimonials</span><span class="nav-sub">what client say</span></div>
    <div class="nav-item active"><span class="nav-title">Book Online</span><span class="nav-sub">book appoiment</span></div>
  </nav>
</header>

<section class="portfolio-strip">
  <div class="portfolio-tile tile-1" role="img" aria-label="Portfolio photo: makeup portrait"></div>
  <div class="portfolio-tile tile-2" role="img" aria-label="Portfolio photo: makeup portrait"></div>
  <div class="portfolio-tile tile-3" role="img" aria-label="Portfolio photo: makeup portrait"></div>
  <div class="portfolio-tile tile-4" role="img" aria-label="Portfolio photo: makeup portrait"></div>
  <div class="portfolio-tile tile-5" role="img" aria-label="Portfolio photo: makeup portrait"></div>
  <div class="portfolio-tile tile-6" role="img" aria-label="Portfolio photo: makeup portrait"></div>
  <div class="portfolio-tile tile-7" role="img" aria-label="Portfolio photo: makeup portrait"></div>
  <div class="portfolio-tile tile-8" role="img" aria-label="Portfolio photo: makeup portrait"></div>
  <div class="portfolio-tile tile-9" role="img" aria-label="Portfolio photo: makeup portrait"></div>
  <div class="portfolio-tile tile-10" role="img" aria-label="Portfolio photo: makeup portrait"></div>
</section>
<div class="strip-base"></div>

<h1 class="page-title">Book Appointment Online</h1>

<section class="booking">
  <div class="booking-bar">Select Appointments: 1 Guest (Just me)</div>
  <div class="search-panel">
    <span class="field-label" style="left:0;top:9px">What kind?</span>
    <span class="service-name">Cut and Style</span>
    <span class="service-meta">(60 mins, $65.00)</span>
    <span class="modify-link">‹ Modify Search or Start Over</span>
    <span class="field-label" style="left:179px;top:13px">With whom?</span>
    <div class="select-box" style="left:181px;top:29px;width:96px">Anyone</div>
    <span class="field-label" style="left:306px;top:11px">When?</span>
    <div class="date-input">1/7/2015</div>
    <svg class="footer-icon" style="left:422px;top:27px" width="14" height="12" viewBox="0 0 14 12"><rect x=".5" y=".5" width="13" height="11" fill="#fff" stroke="#333"/><path d="M1 4h12M4 1v10M7 1v10M10 1v10M1 7h12" stroke="#333" stroke-width=".8"/></svg>
    <div class="select-box" style="left:304px;top:46px;width:146px">Morning (Opening hour to noon)</div>
  </div>
</section>

<div class="day-tabs">
  <span class="day-arrow">‹</span>
  <div class="day-tab">Sun<br>1/4</div>
  <div class="day-tab">Mon<br>1/5</div>
  <div class="day-tab">Tue<br>1/6</div>
  <div class="day-tab current">Wed<br>1/7</div>
  <div class="day-tab">Thu<br>1/8</div>
  <div class="day-tab">Fri<br>1/9</div>
  <div class="day-tab">Sat<br>1/10</div>
  <span class="day-arrow">›</span>
</div>

<h2 class="results-heading" style="font-weight:400">Available appointments on Wednesday, January 07, 2015</h2>
<table class="slots">
  <thead><tr><th style="width:113px">Start</th><th style="width:118px">End</th><th style="width:86px">With</th><th></th></tr></thead>
  <tbody>
    <tr><td>9:00 am</td><td>10:00 am</td><td>studiomae</td><td><span class="select-button">Select</span></td></tr>
    <tr><td>9:00 am</td><td>10:00 am</td><td>studiomae</td><td><span class="select-button">Select</span></td></tr>
    <tr><td>9:00 am</td><td>10:00 am</td><td>studiomae</td><td><span class="select-button">Select</span></td></tr>
    <tr><td>9:00 am</td><td>10:00 am</td><td>studiomae</td><td><span class="select-button">Select</span></td></tr>
  </tbody>
</table>

<aside class="sidebar">
  <div class="sidebar-head"><span class="head-icon" style="color:#999;font-size:12px;top:0">?</span>How Do I...</div>
  <ul class="help-list">
    <li>View a previous booking?</li>
    <li>Reserve multiple services?</li>
    <li>View descriptions of services or packages?</li>
  </ul>
  <div class="sidebar-head"><svg class="head-icon" width="12" height="13" viewBox="0 0 12 13"><circle cx="6" cy="4" r="3" fill="#999"/><path d="M0 13c0-4 2.5-5.5 6-5.5S12 9 12 13z" fill="#999"/></svg>My Appointments</div>
  <p style="margin-top:16px">View upcoming appointments or quickly re-book past appointments.</p>
  <p>If you've already booked with us, <span class="login">Log in »</span></p>
</aside>

<footer class="site-footer">
  <svg class="footer-icon" style="left:240px;top:19px" width="17" height="17" viewBox="0 0 17 17"><circle cx="8.5" cy="8.5" r="7.5" fill="none" stroke="#888" stroke-width="1.5"/><path d="M8.5 4v5h3.5" fill="none" stroke="#888" stroke-width="1.5"/></svg>
  <div class="hours">Mon - Fri : 9:00am to 7:00pm<br><span>Sat</span>: 8:00am to 4:00pm<br><span>Sun</span>: Closed</div>
  <svg class="footer-icon" style="left:241px;top:90px" width="16" height="12" viewBox="0 0 16 12"><rect x=".5" y=".5" width="15" height="11" rx="1" fill="none" stroke="#888"/><path d="M1 4h14" stroke="#888" stroke-width="2"/></svg>
  <div class="cards">
    <div class="card" style="background:#e8e8ee"></div>
    <div class="card" style="background:#d9d9d9"></div>
    <div class="card" style="background:#e7e1d8"></div>
  </div>
  <svg class="footer-icon" style="left:506px;top:19px" width="11" height="16" viewBox="0 0 11 16"><path d="M5.5 0a5.5 5.5 0 0 0-5.5 5.5C0 10 5.5 16 5.5 16S11 10 11 5.5A5.5 5.5 0 0 0 5.5 0z" fill="#888"/><circle cx="5.5" cy="5.5" r="2" fill="#1f1f1f"/></svg>
  <div class="address">Lorem ipsum dolor sit amet, consec-<br>tetuer adipiscing elit, sed diam,<br>nonummy nibh euismod tincidunt</div>
  <svg class="footer-icon" style="left:503px;top:75px" width="18" height="13" viewBox="0 0 18 13"><path d="M1 4c4-4 12-4 16 0l-2 2-3-1V3H6v2L3 6z" fill="#888"/><rect x="4" y="7" width="10" height="6" rx="1" fill="#888"/></svg>
  <div class="phone">0123 456 789</div>
  <div class="social">
    <div class="social-square" role="img" aria-label="Social link"></div>
    <div class="social-square" role="img" aria-label="Social link"></div>
    <div class="social-square" role="img" aria-label="Social link"></div>
    <div class="social-square" role="img" aria-label="Social link"></div>
    <div class="social-square" role="img" aria-label="Social link"></div>
    <div class="social-square" role="img" aria-label="Social link"></div>
  </div>
  <div class="stores">
    <div class="store-badge" role="img" aria-label="App store badge"></div>
    <div class="store-badge" role="img" aria-label="App store badge"></div>
  </div>
</footer>
<div class="copyright">Copyright © 2014 by Clara Mae. All rights reserved.</div>

</body>
</html>
```